Therapy Games Business Needs a Flyer for Conference Bag

Kindle Paths is an on-line business which provides resources and training for professionals who provide therapy to children and adolescents. I am putting a flyer into a conference bag and would like to let the conference attendees know about our resources which are all available online. The conference is called Bright Minds at Class and attendees would by psychologists, school counsellors, and staff associated with student well-being.
The main products I would like promoted are games on social skills and anger management - including -Grumpy Critters, Hint Tiles, Boiling Over or Cooling Off, Feelings Lotto (all can be viewed at www.kindlepaths.com.au).
The aim is to get them to the website to buy however signing up for the e-newsletter is very important.

Industry/Entity Type

Training

```html
<!DOCTYPE html>
<html lang="en">
<head>
<meta charset="utf-8">
<title>Kindle Paths – Conference Flyer</title>
<link href="https://fonts.googleapis.com/css2?family=Arimo:wght@400;700&family=Titan+One&display=swap" rel="stylesheet">
<style>
  :root {
    --page-bg: #e4e4e4;
    --paper: #ffffff;
    --brand-green: #2a7b3e;
    --leaf-green: #5fae57;
    --teal: #4fbf8c;
    --band-green: #3c9a55;
    --deep-green: #2f7f46;
    --bloom-purple: #9a3f7f;
    --bloom-purple-light: #b25a98;
    --grey-text: #6b6b6b;
    --white: #ffffff;
    --label: #111111;
  }
  * { margin: 0; padding: 0; box-sizing: border-box; }
  html, body { width: 1200px; height: 1000px; overflow: hidden; }
  body {
    position: relative;
    background: var(--page-bg);
    font-family: "Arimo", Arial, sans-serif;
  }
  .flyer {
    position: absolute;
    background: var(--paper);
    overflow: hidden;
    box-shadow: 10px 12px 18px rgba(0,0,0,0.28);
  }
  .side-label {
    position: absolute;
    font-size: 40px;
    color: var(--label);
    letter-spacing: 1px;
    transform: translateX(-50%);
  }

  /* Front */
  .flyer--front { left: 27px; top: 170px; width: 562px; height: 727px; }
  .front__header { position: absolute; left: 0; top: 0; width: 100%; height: 170px; background: var(--paper); }
  .brand { position: absolute; display: flex; align-items: center; gap: 10px; color: var(--grey-text); font-weight: 400; }
  .brand__mark { background: var(--leaf-green); }
  .front__brand { left: 50%; top: 104px; transform: translateX(-50%); font-size: 30px; }
  .front__brand .brand__mark { width: 22px; height: 22px; }
  .front__field { position: absolute; left: 0; top: 170px; width: 100%; height: 380px; background: var(--teal); }
  .front__band { position: absolute; left: 0; top: 550px; width: 100%; height: 52px; background: var(--band-green); }
  .front__footer { position: absolute; left: 0; top: 602px; width: 100%; height: 125px; background: var(--deep-green); }
  .front__bloom { position: absolute; left: 18px; top: 172px; width: 526px; height: 450px; }
  .front__headline { position: absolute; left: 0; width: 100%; text-align: center; color: var(--white); }
  .front__we { top: 292px; font-size: 104px; font-weight: 700; line-height: 1; letter-spacing: -2px; }
  .front__provide { top: 395px; font-size: 31px; font-weight: 400; }
  .front__tagline { position: absolute; left: 0; width: 100%; text-align: center; color: var(--white); }
  .front__tagline--lead { top: 636px; font-size: 20px; font-weight: 700; }
  .front__tagline--audience { top: 668px; font-family: "Titan One", "Arimo", sans-serif; font-size: 27px; letter-spacing: 1px; }

  /* Back */
  .flyer--back { left: 607px; top: 57px; width: 561px; height: 726px; }
  .back__scene { position: absolute; left: 0; top: 370px; width: 100%; height: 275px; }
  .back__brand { right: 32px; top: 71px; font-size: 19px; }
  .back__brand .brand__mark { width: 14px; height: 14px; }
  .back__we { position: absolute; left: 38px; top: 78px; font-size: 100px; font-weight: 700; line-height: 1; color: var(--brand-green); letter-spacing: -2px; }
  .back__intro { position: absolute; left: 226px; top: 146px; font-size: 18px; color: var(--brand-green); }
  .back__topic { position: absolute; left: 50px; top: 183px; font-size: 18px; color: var(--brand-green); }
  .game-list { position: absolute; left: 56px; top: 220px; list-style: none; }
  .game-list li { display: flex; align-items: center; height: 37px; font-size: 18px; color: var(--brand-green); }
  .game-list svg { width: 17px; height: 17px; margin-right: 19px; flex: none; }
  .back__visit { position: absolute; left: 0; width: 100%; top: 620px; text-align: center; font-size: 16px; color: var(--white); }
  .back__url-band { position: absolute; left: 0; top: 643px; width: 100%; height: 42px; background: var(--paper); text-align: center; font-size: 25px; font-weight: 700; line-height: 42px; color: var(--brand-green); }
  .back__signup { position: absolute; left: 0; top: 685px; width: 100%; height: 41px; background: var(--band-green); text-align: center; font-size: 19px; line-height: 38px; color: var(--white); }
</style>
</head>
<body>

  <section class="flyer flyer--front">
    <div class="front__header">
      <div class="brand front__brand"><span class="brand__mark"></span>Kindle Paths</div>
    </div>
    <div class="front__field"></div>
    <div class="front__band"></div>
    <div class="front__footer"></div>
    <svg class="front__bloom" viewBox="0 0 526 450" role="img" aria-label="Layered paper flower illustration: large green petals around a purple bloom">
      <defs>
        <radialGradient id="leafGlow" cx="50%" cy="50%" r="50%">
          <stop offset="0%" stop-color="#6cb862"/>
          <stop offset="100%" stop-color="#54a352"/>
        </radialGradient>
        <radialGradient id="bloomGlow" cx="50%" cy="45%" r="55%">
          <stop offset="0%" stop-color="var(--bloom-purple-light)"/>
          <stop offset="100%" stop-color="var(--bloom-purple)"/>
        </radialGradient>
      </defs>
      <ellipse cx="263" cy="215" rx="258" ry="215" fill="url(#leafGlow)"/>
      <ellipse cx="263" cy="200" rx="160" ry="175" fill="url(#bloomGlow)"/>
    </svg>
    <div class="front__headline front__we">WE</div>
    <div class="front__headline front__provide">PROVIDE</div>
    <p class="front__tagline front__tagline--lead">Resources &amp; Training for</p>
    <p class="front__tagline front__tagline--audience">PROFESSIONALS</p>
  </section>
  <div class="side-label" style="left:308px; top:907px;">FRONT</div>

  <section class="flyer flyer--back">
    <svg class="back__scene" viewBox="0 0 561 275" preserveAspectRatio="none" role="img" aria-label="Sweeping coloured ribbons with game boxes and an adult silhouette playing a board game with two children">
      <defs>
        <linearGradient id="sceneFade" x1="0" y1="0" x2="0" y2="1">
          <stop offset="0%" stop-color="#ffffff" stop-opacity="0"/>
          <stop offset="45%" stop-color="#dcefd9"/>
          <stop offset="100%" stop-color="#4f9f55"/>
        </linearGradient>
      </defs>
      <rect width="561" height="275" fill="url(#sceneFade)"/>
    </svg>
    <div class="brand back__brand"><span class="brand__mark"></span>Kindle Paths</div>
    <div class="back__we">WE</div>
    <p class="back__intro">give training for games on</p>
    <p class="back__topic">Social skills &amp; Anger management</p>
    <ul class="game-list">
      <li><svg viewBox="0 0 18 18"><circle cx="9" cy="9" r="8" fill="none" stroke="#2a7b3e" stroke-width="1.6"/><path d="M7 5l4 4-4 4" fill="none" stroke="#2a7b3e" stroke-width="2"/></svg>Grumpy Critters,</li>
      <li><svg viewBox="0 0 18 18"><circle cx="9" cy="9" r="8" fill="none" stroke="#2a7b3e" stroke-width="1.6"/><path d="M7 5l4 4-4 4" fill="none" stroke="#2a7b3e" stroke-width="2"/></svg>Hint Tiles,</li>
      <li><svg viewBox="0 0 18 18"><circle cx="9" cy="9" r="8" fill="none" stroke="#2a7b3e" stroke-width="1.6"/><path d="M7 5l4 4-4 4" fill="none" stroke="#2a7b3e" stroke-width="2"/></svg>Boiling Over or Cooling Off</li>
      <li><svg viewBox="0 0 18 18"><circle cx="9" cy="9" r="8" fill="none" stroke="#2a7b3e" stroke-width="1.6"/><path d="M7 5l4 4-4 4" fill="none" stroke="#2a7b3e" stroke-width="2"/></svg>Feelings Lotto</li>
    </ul>
    <p class="back__visit">visit</p>
    <div class="back__url-band">www.kindlepaths.com.au</div>
    <div class="back__signup">Signup for e-newsletter</div>
  </section>
  <div class="side-label" style="left:865px; top:805px;">BACK</div>

</body>
</html>
```